Law Firm Marketing Post Card to Real Estate Agents

We need a postcard that will be used to market to real estate agents. Something clean, professional and appealing. We're marketing for a specific field (taxes) and are planning on passing out the cards to individual agents and we do not plan on mailing them. We'd like something on the front cover that truly catches someones attention and makes them want to read the back side. Text will read:

Front and Back; front will have very little text. Only the following:
Tax & Legal Strategies for Real Estate Agents
Presented by Bluefield Law Partners, LLC
5 Tax Strategies Every Real Estate Agent Should Know

BACK COVER:
Most real estate agents are considered 1099 independent contractors, and have never been told that there are money saving strategies that could make a huge difference for them come tax time with just a few easy steps.

With our free consultation, Bluefield has one mission – to teach real estate agents 5 legal and tax planning strategies that could literally save them thousands of dollars.

Please contact us to schedule a one-on-one consultation, or an office presentation, and learn about some of the tax and legal strategies that have helped countless real estate agents and independent contractors:

- Minimize self employment tax
- Deduct 100% of out of pocket medical expenses
- Create wealth
- Deduct 100% of health insurance premiums
- Invest in real estate
- Deduct a portion of a child’s tuition and expenses
- Reduce overall tax liability

For more information, please email our office at: Info@BluefieldPartners.Org.

Target Market(s)

Real Estate Agents

Industry/Entity Type

Real Estate

Requirements
Must have
• Text listed on the front of the card as shown on the attachment.
• Clean, appealing, professional cover.
• must be similar to colors used on our website so that the reader feels like it is from the same company; please include website address on card as well - www.bluefieldpartners.org

```html
<!DOCTYPE html>
<html lang="en">
<head>
<meta charset="utf-8">
<title>Bluefield Law Partners – Postcard</title>
<link rel="stylesheet" href="https://fonts.googleapis.com/css2?family=Antonio:wght@600&family=Source+Sans+3:ital,wght@0,400;0,600;0,700;1,400&display=swap">
<style>
  :root {
    --backdrop: #231f20;
    --navy: #1d355f;
    --blue: #3a5d95;
    --blue-light: #5f83bb;
    --white: #ffffff;
    --ink: #2a3d66;
  }
  * { margin: 0; padding: 0; box-sizing: border-box; }
  html, body { width: 801px; height: 1200px; overflow: hidden; }
  body { background: var(--backdrop); position: relative; font-family: "Source Sans 3", Arial, sans-serif; }

  .card { position: absolute; left: 51px; width: 699px; height: 537px; overflow: hidden; }
  .card-front { top: 45px; }
  .card-back { top: 621px; background: var(--white); }
  .card-art { position: absolute; inset: 0; }

  .headline {
    position: absolute; right: 26px; text-align: right; white-space: nowrap;
    font-family: "Antonio", "Arial Narrow", sans-serif; font-weight: 600;
    color: var(--white); text-transform: uppercase;
  }
  .headline-top { top: 64px; font-size: 45px; line-height: 52px; letter-spacing: -0.6px; }
  .headline-bottom { top: 364px; font-size: 40px; line-height: 49px; letter-spacing: -0.5px; }

  .presenter { position: absolute; left: 410px; top: 256px; }
  .presenter-label { font-style: italic; font-size: 16px; color: var(--ink); }
  .presenter-name {
    display: flex; align-items: center; gap: 7px; margin-top: 8px;
    font-size: 17px; font-weight: 700; color: var(--ink); white-space: nowrap;
  }
  .presenter-mark { width: 15px; height: 15px; background: var(--ink); }

  .back-copy { position: absolute; left: 37px; top: 0; color: var(--white); font-size: 12.6px; line-height: 17px; }
  .back-copy p, .back-copy ul { position: absolute; left: 0; }
  .back-copy p { text-align: justify; }
  .copy-intro { top: 53px; width: 364px; }
  .copy-mission { top: 138px; width: 349px; }
  .copy-contact { top: 220px; width: 336px; }
  .benefits { top: 319px; width: 340px; list-style: none; font-weight: 600; font-size: 12.8px; white-space: nowrap; }
  .benefits li { position: relative; padding-left: 21px; line-height: 17px; }
  .benefits li::before {
    content: ""; position: absolute; left: 3px; top: 5px;
    width: 8px; height: 8px; border-radius: 50%; background: var(--white);
  }

  .stamp-box { position: absolute; left: 570px; top: 54px; width: 96px; height: 95px; background: #000; }
  .address-line { position: absolute; left: 411px; width: 256px; height: 1px; background: #000; }

  .footer-band {
    position: absolute; left: 0; top: 470px; width: 699px; height: 67px;
    background: linear-gradient(90deg, var(--blue-light), #4d72ad 50%, var(--blue-light));
    color: var(--white); font-weight: 700; font-size: 22px;
    display: flex; align-items: center; justify-content: center; white-space: nowrap;
  }
</style>
</head>
<body>

<section class="card card-front">
  <svg class="card-art" width="699" height="537" viewBox="0 0 699 537">
    <defs>
      <linearGradient id="panelBlue" x1="0" y1="0" x2="1" y2="1">
        <stop offset="0" stop-color="#2d4e86"/>
        <stop offset="0.5" stop-color="#4e72ad"/>
        <stop offset="1" stop-color="#2f5089"/>
      </linearGradient>
      <linearGradient id="skyline" x1="0" y1="0" x2="1" y2="1">
        <stop offset="0" stop-color="#4c86cf"/>
        <stop offset="0.45" stop-color="#2b5ea8"/>
        <stop offset="0.7" stop-color="#a99882"/>
        <stop offset="1" stop-color="#6b6154"/>
      </linearGradient>
      <linearGradient id="silverBand" x1="0" y1="0" x2="0" y2="1">
        <stop offset="0" stop-color="#bfc0c3"/>
        <stop offset="0.5" stop-color="#f4f4f5"/>
        <stop offset="1" stop-color="#cfd0d2"/>
      </linearGradient>
    </defs>
    <rect width="699" height="537" fill="url(#panelBlue)"/>
    <polygon points="0,0 247,0 341,537 0,537" fill="url(#skyline)" role="img" aria-label="Photograph of modern glass office towers against a blue sky"/>
    <polygon points="247,0 257,0 351,537 341,537" fill="var(--white)"/>
    <polygon points="259,203 699,203 699,334 282,334" fill="url(#silverBand)"/>
  </svg>

  <h1 class="headline headline-top">Tax &amp; Legal Strategies<br>for Real Estate Agents</h1>

  <div class="presenter">
    <div class="presenter-label">Presented by</div>
    <div class="presenter-name"><span class="presenter-mark"></span>Bluefield Law Partners, LLC</div>
  </div>

  <h2 class="headline headline-bottom">5 Tax Strategies Every<br>Real Estate Agent<br>Should Know</h2>
</section>

<section class="card card-back">
  <svg class="card-art" width="699" height="537" viewBox="0 0 699 537">
    <defs>
      <linearGradient id="backBlue" x1="0" y1="0" x2="0.6" y2="1">
        <stop offset="0" stop-color="#44679f"/>
        <stop offset="1" stop-color="#1b3360"/>
      </linearGradient>
    </defs>
    <polygon points="0,0 446,0 363,470 0,470" fill="url(#backBlue)"/>
    <polygon points="446,0 453,0 370,470 363,470" fill="#9aa4b3"/>
  </svg>

  <div class="back-copy">
    <p class="copy-intro">Most real estate agents are considered 1099 independent contractors, and have never been told that there are money saving strategies that could make a huge difference for them come tax time with just a few easy steps.</p>
    <p class="copy-mission">With our free consultation, Bluefield has one mission – to teach real estate agents 5 legal and tax planning strategies that could literally save them thousands of dollars.</p>
    <p class="copy-contact">Please contact us to schedule a one-on-one consultation, or an office presentation, and learn about some of the tax and legal strategies that have helped countless real estate agents and independent contractors:</p>
    <ul class="benefits">
      <li>Minimize self employment tax</li>
      <li>Deduct 100% of out of pocket medical expenses</li>
      <li>Create wealth</li>
      <li>Deduct 100% of health insurance</li>
      <li>Invest in real estate</li>
      <li>Deduct a portion of a child’s tuition and expenses</li>
      <li>Reduce overall tax liability</li>
    </ul>
  </div>

  <div class="stamp-box"></div>
  <div class="address-line" style="top:358px"></div>
  <div class="address-line" style="top:397px"></div>
  <div class="address-line" style="top:436px"></div>

  <div class="footer-band">For more information email at: Info@BluefieldPartners.Org.</div>
</section>

</body>
</html>
```